Dental Business Card

We are looking for a double sided business card that can be easily customized with the names of the different members of our dental team.

I would like the background to be the 2-tone blue fleur-de-lis type pattern on the sides of our website (www.harborvalebrights.com).

I would like the logo attached incorporated.

I would like our address (2847 Birchmont Court, Suite 240, Fairhaven, ME 04011), phone number (555-318-4902), fax number (555-318-4977), website (www.harborvalebrights.com), and email address (info@harborvalebrights.com) all included on the front side.

Something a little more artistic to complement/highlight the logo on the back would be interesting.

I would like the business card to look professional, slightly feminine, and expense.

```html
<!DOCTYPE html>
<html lang="en">
<head>
<meta charset="utf-8">
<title>Harborvale Brights — Business Card</title>
<link rel="stylesheet" href="https://fonts.googleapis.com/css2?family=Cinzel:wght@600&family=Open+Sans:wght@400&display=swap">
<style>
  :root {
    --page: #e6e6e6;
    --back-card: #3b3b3d;
    --back-ink: #141414;
    --front-card: #c8dcea;
    --front-card-deep: #b7d0e2;
    --navy: #1f4f9a;
    --mid-blue: #2f76c4;
    --text-dark: #1e3f78;
  }
  * { box-sizing: border-box; margin: 0; padding: 0; }
  html, body { width: 1200px; height: 1000px; overflow: hidden; }
  body {
    background: var(--page);
    display: flex; flex-direction: column; align-items: center; justify-content: center;
    gap: 60px;
  }
  .card {
    position: relative;
    width: 770px; height: 440px;
    border-radius: 4px;
    box-shadow: 0 6px 18px rgba(0,0,0,.18);
    overflow: hidden;
  }

  /* Back side */
  .card--back { background: var(--back-card); color: var(--back-ink); }
  .back-mark {
    position: absolute; left: 50%; top: 48px; transform: translateX(-50%);
    width: 170px; height: 170px; border-radius: 50%;
    background: var(--back-ink);
  }
  .back-name {
    position: absolute; left: 0; right: 0; top: 250px; text-align: center;
    font: 600 50px/1 "Cinzel", serif; letter-spacing: 1px;
  }
  .back-tagline {
    position: absolute; left: 0; right: 0; top: 322px;
    display: flex; align-items: center; justify-content: center; gap: 22px;
    font: 600 26px/1 "Cinzel", serif; letter-spacing: 1px;
  }
  .back-tagline .rule { width: 140px; height: 2px; background: var(--back-ink); }

  /* Front side */
  .card--front { background: var(--front-card); color: var(--text-dark); }
  .front-pattern {
    position: absolute; inset: 0;
    background: radial-gradient(circle at 50% 50%, var(--front-card) 0%, var(--front-card-deep) 100%);
  }
  .front-brand { position: absolute; left: 40px; top: 40px; }
  .front-name {
    font: 600 38px/1 "Cinzel", serif; color: var(--navy); letter-spacing: .5px;
  }
  .front-tagline {
    margin-top: 8px; padding-left: 110px;
    display: flex; align-items: center; gap: 14px;
    font: 600 20px/1 "Cinzel", serif; color: var(--navy);
  }
  .front-tagline .rule { width: 130px; height: 2px; background: var(--mid-blue); }
  .front-mark {
    position: absolute; right: 80px; top: 110px;
    width: 190px; height: 190px; border-radius: 50%;
    background: var(--mid-blue);
  }
  .contact-list {
    position: absolute; left: 40px; top: 205px; list-style: none;
    font: 400 20px/1.3 "Open Sans", sans-serif; color: var(--text-dark);
  }
  .contact-list li { display: flex; align-items: center; gap: 12px; }
  .contact-list svg { width: 18px; height: 18px; flex: none; }
  .front-address {
    position: absolute; left: 40px; bottom: 38px;
    font: 400 21px/1 "Open Sans", sans-serif; color: var(--text-dark); letter-spacing: .5px;
  }
</style>
</head>
<body>

  <section class="card card--back" aria-label="Business card back">
    <div class="back-mark"></div>
    <h1 class="back-name">HARBORVALE BRIGHTS</h1>
    <p class="back-tagline"><span class="rule"></span>CARE WITH ELEGANCE<span class="rule"></span></p>
  </section>

  <section class="card card--front" aria-label="Business card front">
    <div class="front-pattern" role="img" aria-label="Two-tone light blue fleur-de-lis damask pattern background"></div>

    <div class="front-brand">
      <h2 class="front-name">HARBORVALE BRIGHTS</h2>
      <p class="front-tagline">CARE WITH ELEGANCE<span class="rule"></span></p>
    </div>

    <div class="front-mark"></div>

    <ul class="contact-list">
      <li>
        <svg viewBox="0 0 20 20"><circle cx="10" cy="10" r="10" fill="#1e3f78"/><path d="M7 5l2 2-1 1.5c.6 1.4 1.6 2.4 3 3L12.5 10l2 2-1.2 1.8C9.5 13.5 6.5 10.5 5.8 6.3z" fill="#fff"/></svg>
        555-318-4902
      </li>
      <li>
        <svg viewBox="0 0 20 20"><circle cx="10" cy="10" r="10" fill="#1e3f78"/><rect x="6" y="5" width="8" height="4" fill="#fff"/><rect x="5" y="9" width="10" height="6" rx="1" fill="#fff"/></svg>
        555-318-4977
      </li>
      <li>
        <svg viewBox="0 0 20 20"><circle cx="10" cy="10" r="10" fill="#1e3f78"/><rect x="5" y="6.5" width="10" height="7" fill="#fff"/><path d="M5 6.5l5 4 5-4" stroke="#1e3f78" fill="none"/></svg>
        info@harborvalebrights.com
      </li>
      <li>
        <svg viewBox="0 0 20 20"><circle cx="10" cy="10" r="10" fill="#1e3f78"/><circle cx="9" cy="9" r="3" stroke="#fff" stroke-width="1.6" fill="none"/><path d="M11.2 11.2l3 3" stroke="#fff" stroke-width="1.8"/></svg>
        www.harborvalebrights.com
      </li>
    </ul>

    <p class="front-address">2847 BIRCHMONT COURT, SUITE 240, FAIRHAVEN, ME 04011</p>
  </section>

</body>
</html>
```